Talvora Cellars WIX website

We are opening a new winery called Talvora Cellars. We think that "Wine should be an experience..." To aid in that experience, each bottle of wine label will have a unique QR code that directs patrons to a page on the site that highlights the wines. On this page each wine bottle will be displayed, the winemaking notes will be included. Also included will be food pairings with recipes, movie and music ideas and anything else that will add to the experience. I need a website that helps showcase annual wines, has a members only area (for the wine club) and allows people to purchase wine on-line. I've started the beginning of a site on WIX - talvoracellars-demo.com. There's no requirement or expectation to simply finish what I've started. I just needed to get something up and live. Let your imagination take over. I want to unique site and kicks a*s...
Updates

Logo font is Trajan Pro...

I'm open to any designs, meaning don't feel like you have to complete what I started.

I want to keep the logo and the font, however...

Other fonts used should compliment Trajan Pro.

Font styles to use
Serif
Other font styles liked:
• Trajan Pro is what was used for the logo

Requirements
Must have
• Attractive and compelling home page, red wine section, white wine section, members only area, page that speaks of and allows purchase into a wine club, all easy enough for me to edit and add pages without coding knowledge. Adding pages is why I chose WIX as the platform. Here is a list of the pages or tabs: About, Events, Vintner’s Circle, Press/Accolades, Wines - Red/White/Dessert/Summer Series (as sub pages), Contact

```html
<!DOCTYPE html>
<html lang="en">
<head>
<meta charset="utf-8">
<title>Talvora Cellars – Home</title>
<link href="https://fonts.googleapis.com/css2?family=Cinzel:wght@400;500&family=Montserrat:wght@400;500;600&display=swap" rel="stylesheet">
<style>
:root{
  --stage:#c8c8c8;
  --wine:#8a2330;
  --gold:#a98a5a;
  --gold-light:#c6ab7c;
  --gold-mid:#b0915c;
  --gold-deep:#a5844d;
  --cream:#f6efe4;
  --card:#f2e9d8;
  --ink:#2b2420;
  --muted:#6d625a;
  --black:#111;
  --white:#fff;
}
*{margin:0;padding:0;box-sizing:border-box}
html,body{width:1200px;height:2809px;overflow:hidden;background:var(--stage)}
body{font-family:"Montserrat",sans-serif;color:var(--ink)}
.canvas{position:relative;width:1200px;height:2809px;overflow:hidden;background:var(--stage)}
.site{position:absolute;background:var(--white);overflow:hidden}
.site-desktop{left:293px;top:68px;width:505px;height:2674px}
.site-mobile{left:919px;top:68px;width:146px;height:2678px}
.section{position:relative;width:100%;overflow:hidden}
.abs{position:absolute}
.serif{font-family:"Cinzel",serif;font-weight:400}
.eyebrow{position:absolute;left:0;right:0;text-align:center;font-size:5.5px;letter-spacing:1.4px;color:var(--gold);text-transform:uppercase;white-space:nowrap}
.eyebrow.left{text-align:left}
.title{position:absolute;left:0;right:0;text-align:center;font-family:"Cinzel",serif;color:var(--ink);letter-spacing:1px;white-space:nowrap}
.title.left{text-align:left}
.rule{position:absolute;height:1px;background:var(--gold)}
.underline{position:absolute;left:50%;height:1px;width:40px;margin-left:-20px;background:var(--gold)}
.lorem{position:absolute;font-size:5px;line-height:1.45;color:var(--muted)}
.center{text-align:center}
.pill{position:absolute;border-radius:20px;background:var(--gold);color:var(--white);font-size:4.2px;letter-spacing:1px;text-transform:uppercase;display:flex;align-items:center;justify-content:center;font-weight:600;white-space:nowrap}
.pill.outline{background:transparent;border:1px solid var(--ink);color:var(--ink)}
.pill.outline-light{background:transparent;border:1px solid var(--white);color:var(--white)}
.photo{position:absolute}
.bottle{position:absolute;left:50%;border-radius:7px 7px 3px 3px}
.bottle.red{background:linear-gradient(180deg,#1a0b0d 0%,#3b1016 35%,#efe9df 52%,#e5ddd0 75%,#2a0c10 90%,#1a0b0d 100%)}
.bottle.rose{background:linear-gradient(180deg,#3d0a12 0%,#8a1f2d 35%,#efe9df 52%,#e5ddd0 75%,#6e1823 90%,#3d0a12 100%)}
.bottle.green{background:linear-gradient(180deg,#c9a95a 0%,#c9a95a 14%,#1c4428 30%,#efe9df 55%,#e5ddd0 78%,#1c4428 90%,#0f2a18 100%)}
.bottle.white{background:linear-gradient(180deg,#2c2c2c 0%,#3a3a34 12%,#dfe2b4 28%,#f3f1e2 52%,#ece8d6 75%,#d4d7a2 90%,#c4c79a 100%)}
.brand{position:absolute;text-align:center;font-family:"Cinzel",serif;color:var(--white);letter-spacing:1px;line-height:1.05}

/* desktop */
.d-hero{height:314px;background:var(--black)}
.d-nav{position:absolute;top:26px;font-size:4.6px;letter-spacing:.6px;color:var(--white);text-transform:uppercase;display:flex;gap:14px;align-items:center;white-space:nowrap}
.d-nav .dot{width:2px;height:2px;border-radius:50%;background:var(--white)}
.d-nav .active{border-bottom:1px solid var(--gold);padding-bottom:3px;margin-top:3px}
.d-featured{height:324px}
.f-card{position:absolute;top:92px;width:104px;height:156px;background:var(--card);border:1px solid #e5d7bd}
.f-card::after{content:"";position:absolute;inset:3px;border:1px solid #e8dcc5;pointer-events:none}
.f-card .name{position:absolute;top:100px;left:0;right:0;text-align:center;font-size:5.4px;letter-spacing:1.2px;font-weight:500}
.f-card .lorem{top:110px;left:10px;right:10px;text-align:center;font-size:4.2px}
.f-card .pill{top:131px;left:32px;width:40px;height:9px;font-size:3.6px}
.d-maker{height:265px;background:var(--cream)}
.d-cats{height:230px}
.cat{position:absolute;top:17px;height:191px;width:150px}
.cat .title{top:20px;color:var(--white);font-size:12.5px}
.cat .lorem{top:42px;left:18px;right:18px;text-align:center;color:#f3e8de;font-size:5px}
.cat .pill{top:65px;left:46px;width:58px;height:13px;font-size:4px}
.d-member{height:264px}
.d-annual{height:289px}
.arch{position:absolute;top:86px;width:134px;height:176px;border-radius:67px 67px 0 0;background:var(--card);border:1px solid #e5d7bd}
.arch .name{position:absolute;top:117px;left:0;right:0;text-align:center;font-size:5.6px;letter-spacing:1.2px;font-weight:500}
.arch .lorem{top:127px;left:20px;right:20px;text-align:center;font-size:4.2px}
.arch .pill{top:146px;left:38px;width:58px;height:11px;font-size:3.8px}
.chev{position:absolute;width:10px;height:16px}
.d-testi{height:247px}
.d-events{height:283px}
.ev-date{position:absolute;font-size:4px;color:var(--ink);display:flex;gap:3px;align-items:center;white-space:nowrap}
.ev-date i{display:block;width:5px;height:5px;background:var(--gold)}
.ev-title{position:absolute;font-size:6.8px;line-height:1.35;font-weight:500;color:var(--ink)}
.d-exp{height:459px}
.foot-head{position:absolute;font-family:"Cinzel",serif;font-size:7.4px;color:var(--white);letter-spacing:.6px;white-space:nowrap}
.foot-links{position:absolute;font-size:5px;line-height:2.25;color:#d9d3cc}
.social{position:absolute;display:flex;gap:3px}
.social i{display:block;border-radius:50%;background:var(--white)}

/* mobile */
.m-hero{height:217px;background:var(--black)}
.m-featured{height:250px}
.m-maker{height:311px;background:var(--cream)}
.m-cats{height:475px}
.m-cat{position:absolute;left:21px;width:109px;height:139px}
.m-cat .title{top:11px;color:var(--white);font-size:8.6px}
.m-cat .lorem{top:26px;left:12px;right:12px;font-size:3.3px;text-align:center;color:#f3e8de}
.m-cat .pill{top:42px;left:36px;width:38px;height:8px;font-size:2.8px}
.m-member{height:254px}
.m-annual{height:207px}
.m-testi{height:200px}
.m-events{height:280px}
.m-exp{height:484px}

/* photo tones */
.ph-hero{background:linear-gradient(160deg,#0d0304 0%,#2a060b 22%,#7a1020 42%,#a8182b 55%,#4a0a12 68%,#1a0507 80%,#c9a38a 92%,#6b3a2c 100%)}
.ph-toast{background:radial-gradient(circle at 50% 22%,#fbe7b4 0%,#e9bf7c 22%,#b98b5c 42%,#8a5a46 58%,#6b7440 78%,#4c5a2e 100%)}
.ph-club{background:linear-gradient(180deg,#8fa266 0%,#6e8450 18%,#c2b49a 34%,#6d7c8e 46%,#55604a 62%,#3a4030 78%,#1b1b17 100%)}
.ph-valley{background:linear-gradient(180deg,#f4f2ee 0%,#e8e2d7 30%,#b6ada0 48%,#8f8f6a 62%,#687a34 76%,#4f6124 88%,#3f4e1b 100%)}
.ph-sunset{background:linear-gradient(180deg,#6f7e58 0%,#b8a27a 28%,#e0b17a 45%,#9a6a4a 62%,#4a3428 78%,#7c5a44 100%)}
.ph-laugh{background:linear-gradient(135deg,#2d3240 0%,#5d5a60 40%,#a58c72 70%,#3b3a3e 100%)}
.ph-dinner{background:linear-gradient(135deg,#1e1816 0%,#4a3424 40%,#b0834c 65%,#3a2a1c 100%)}
.ph-field{background:linear-gradient(180deg,#f4f1ea 0%,#e5dcc4 10%,#b8ad6a 24%,#8a8a32 38%,#5f6a22 52%,#3a4216 66%,#1a1d0c 78%,#0c0c0c 86%,#0c0c0c 100%)}
.ph-glass{background:linear-gradient(180deg,rgba(255,255,255,.85) 0%,rgba(250,240,200,.95) 35%,rgba(232,214,150,.95) 55%,rgba(255,255,255,.75) 72%,rgba(255,255,255,.35) 100%)}
.ph-redpair{background:linear-gradient(90deg,#a0323e 0%,#5a0f18 30%,#2a0a0e 55%,#160507 75%,#3a1218 100%)}
.ph-whitepair{background:linear-gradient(90deg,#f3efd2 0%,#e6dc9c 35%,#f0e8b8 60%,#d7cd8a 80%,#c9bf7d 100%)}
.ph-sparkpair{background:linear-gradient(90deg,#efe6c4 0%,#e3d3a0 35%,#2e5a3a 60%,#0f2a18 80%,#e9e0b6 100%)}
.ph-face{background:radial-gradient(circle at 50% 40%,#a9a9a9,#5a5a5a 60%,#2e2e2e)}
.ph-sign{background:linear-gradient(90deg,rgba(43,36,32,.2),rgba(43,36,32,.04))}
</style>
</head>
<body>
<div class="canvas">

<!-- Desktop layout -->
<div class="site site-desktop">

  <section class="section d-hero">
    <div class="photo ph-hero" role="img" aria-label="Red wine being poured from a bottle into a glass against deep red fabric" style="inset:0"></div>
    <nav class="d-nav" style="left:50px">
      <span class="active">About</span><span class="dot"></span><span>Events</span><span class="dot"></span><span>Vintner’s Circle</span>
    </nav>
    <div class="brand" style="left:215px;width:75px;top:8px">
      <div style="width:16px;height:16px;border:1px solid #fff;border-radius:50%;margin:0 auto 3px"></div>
      <div style="font-size:9px">TALVORA</div>
      <div style="font-size:4px;letter-spacing:1.8px">CELLARS</div>
    </div>
    <nav class="d-nav" style="left:300px">
      <span>Press</span><span class="dot"></span><span>Wines</span><span class="dot"></span><span>Contact</span>
    </nav>
    <div class="eyebrow" style="top:93px;font-size:6.6px;letter-spacing:1.6px">Introducing Talvora Cellars</div>
    <div class="title" style="top:103px;font-size:19px;color:#fff">Because wine should be</div>
    <div class="title" style="top:124px;font-size:19px;color:#fff">An experience</div>
    <div class="rule" style="top:135px;left:120px;width:40px;background:#fff"></div>
    <div class="rule" style="top:135px;left:345px;width:40px;background:#fff"></div>
    <div class="underline" style="top:150px;background:#fff"></div>
    <div class="abs" style="left:252px;top:286px;width:1px;height:40px;background:var(--gold-light)"></div>
  </section>

  <section class="section d-featured">
    <div class="abs" style="left:252px;top:0;width:1px;height:10px;background:var(--gold-light)"></div>
    <div class="eyebrow" style="top:24px">— Talvora Cellars Wine —</div>
    <div class="title" style="top:33px;font-size:17px">Featured Wines</div>
    <div class="underline" style="top:56px"></div>

    <div class="f-card" style="left:28px">
      <div class="bottle red" role="img" aria-label="Red wine bottle" style="top:-8px;width:26px;margin-left:-13px;height:100px"></div>
      <div class="name">WINE HEADING</div>
      <div class="lorem">Lorem ipsum dolor sit amet consec­tetur adipiscing elit sed</div>
      <div class="pill">Shop Wine</div>
    </div>
    <div class="f-card" style="left:143px">
      <div class="bottle green" role="img" aria-label="Sparkling wine bottle" style="top:-16px;width:28px;margin-left:-14px;height:110px"></div>
      <div class="name">WINE HEADING</div>
      <div class="lorem">Lorem ipsum dolor sit amet consec­tetur adipiscing elit sed</div>
      <div class="pill">Shop Wine</div>
    </div>
    <div class="f-card" style="left:260px">
      <div class="bottle rose" role="img" aria-label="Red wine bottle" style="top:-12px;width:28px;margin-left:-14px;height:106px"></div>
      <div class="name">WINE HEADING</div>
      <div class="lorem">Lorem ipsum dolor sit amet consec­tetur adipiscing elit sed</div>
      <div class="pill">Shop Wine</div>
    </div>
    <div class="f-card" style="left:373px">
      <div class="bottle white" role="img" aria-label="White wine bottle" style="top:-8px;width:24px;margin-left:-12px;height:102px"></div>
      <div class="name">WINE HEADING</div>
      <div class="lorem">Lorem ipsum dolor sit amet consec­tetur adipiscing elit sed</div>
      <div class="pill">Shop Wine</div>
    </div>

    <div class="rule" style="top:263px;left:211px;width:18px;background:#999"></div>
    <div class="rule" style="top:263px;left:240px;width:18px;height:2px;background:var(--gold)"></div>
    <div class="rule" style="top:263px;left:269px;width:18px;background:#999"></div>
    <div class="pill outline" style="top:284px;left:210px;width:83px;height:20px;font-size:5.6px">View All ›</div>
  </section>

  <section class="section d-maker">
    <div class="photo ph-toast" role="img" aria-label="Friends raising wine glasses in a toast at an outdoor vineyard table" style="left:39px;top:33px;width:196px;height:196px;border-radius:50%;border:4px solid var(--gold)"></div>
    <div class="eyebrow left" style="left:263px;top:45px">About our wines —</div>
    <div class="title left" style="left:263px;top:56px;font-size:15.5px;line-height:1.2">Message from the<br>Winemaker</div>
    <div class="rule" style="left:263px;top:100px;width:30px"></div>
    <div class="lorem" style="left:266px;top:117px;width:210px;font-size:6px;color:var(--ink)">I started my winemaking journey with one simple goal in mind - I wanted to make wine as good or better than the wine I could buy. At the time of that goal in 2015, I had no perspective on the path that would form before me.</div>
    <div class="lorem" style="left:266px;top:173px;font-size:6px;color:var(--ink)">Enjoy...the experience.</div>
    <div class="photo ph-face" role="img" aria-label="Portrait of the winemaker" style="left:263px;top:190px;width:32px;height:32px;border-radius:50%"></div>
    <div class="photo ph-sign" role="img" aria-label="Handwritten signature of Julian Talvora" style="left:300px;top:198px;width:100px;height:16px"></div>
  </section>

  <section class="section d-cats">
    <div class="cat" style="left:34px;background:var(--wine)">
      <div class="title">Red Wine</div>
      <div class="lorem">Lorem ipsum dolor sit amet, consecte­tur adipiscing elit, sed do</div>
      <div class="pill outline-light">Try it now</div>
      <div class="photo ph-redpair" role="img" aria-label="Glass of red wine beside a red wine bottle" style="left:46px;top:86px;width:58px;height:105px;border-radius:18px 18px 0 0"></div>
    </div>
    <div class="cat" style="left:183px;background:var(--gold-mid)">
      <div class="title">White Wine</div>
      <div class="lorem">Lorem ipsum dolor sit amet, consecte­tur adipiscing elit, sed do</div>
      <div class="pill outline-light">Try it now</div>
      <div class="photo ph-whitepair" role="img" aria-label="Glass of white wine beside a white wine bottle" style="left:46px;top:86px;width:58px;height:105px;border-radius:18px 18px 0 0"></div>
    </div>
    <div class="cat" style="left:333px;width:151px;background:var(--gold-deep)">
      <div class="title">Summer Series</div>
      <div class="lorem">Lorem ipsum dolor sit amet, consecte­tur adipiscing elit, sed do</div>
      <div class="pill outline-light">Try it now</div>
      <div class="photo ph-sparkpair" role="img" aria-label="Glass of sparkling wine beside a sparkling bottle" style="left:46px;top:86px;width:58px;height:113px;border-radius:18px 18px 0 0"></div>
    </div>
  </section>

  <section class="section d-member">
    <div class="photo ph-club" role="img" aria-label="Friends in hats raising wine glasses in a sunny vineyard" style="inset:0"></div>
    <div class="eyebrow left" style="left:59px;top:183px;color:#fff;font-size:6px">Our wine club</div>
    <div class="title left" style="left:58px;top:192px;font-size:19.5px;color:#fff">Member Only</div>
    <div class="pill" style="left:58px;top:222px;width:81px;height:20px;font-size:5.4px">Read More ›</div>
    <div class="lorem" style="left:275px;top:189px;width:190px;font-size:7px;line-height:1.6;color:#fff">Lorem ipsum dolor sit amet, consectetur adipi­scing elit, sed do eiusmod tempor incididunt ut labore et dolore magna aliqua. o eiusmod tempor incididunt ut labore</div>
  </section>

  <section class="section d-annual">
    <div class="eyebrow" style="top:27px">— Talvora Cellars Wine —</div>
    <div class="title" style="top:36px;font-size:17px">Annual Wines</div>
    <div class="underline" style="top:59px"></div>
    <svg class="chev" style="left:18px;top:164px" viewBox="0 0 10 16"><path d="M8 1 2 8l6 7" fill="none" stroke="#777" stroke-width="1"/></svg>
    <svg class="chev" style="left:477px;top:164px" viewBox="0 0 10 16"><path d="M2 1l6 7-6 7" fill="none" stroke="#777" stroke-width="1"/></svg>
    <div class="arch" style="left:41px">
      <div class="bottle red" role="img" aria-label="Red wine bottle" style="top:12px;width:26px;margin-left:-13px;height:100px"></div>
      <div class="name">WINE HEADING</div>
      <div class="lorem">Lorem ipsum dolor sit amet consec­tetur adipiscing elit sed</div>
      <div class="pill">Shop Wine</div>
    </div>
    <div class="arch" style="left:186px">
      <div class="bottle white" role="img" aria-label="White wine bottle" style="top:12px;width:26px;margin-left:-13px;height:100px"></div>
      <div class="name">WINE HEADING</div>
      <div class="lorem">Lorem ipsum dolor sit amet consec­tetur adipiscing elit sed</div>
      <div class="pill">Shop Wine</div>
    </div>
    <div class="arch" style="left:331px">
      <div class="bottle red" role="img" aria-label="Red wine bottle" style="top:12px;width:26px;margin-left:-13px;height:100px"></div>
      <div class="name">WINE HEADING</div>
      <div class="lorem">Lorem ipsum dolor sit amet consec­tetur adipiscing elit sed</div>
      <div class="pill">Shop Wine</div>
    </div>
  </section>

  <section class="section d-testi">
    <div class="photo ph-valley" role="img" aria-label="Hazy mountains above rows of vineyard" style="inset:0"></div>
    <div class="eyebrow" style="top:24px">— Testimonials —</div>
    <div class="title" style="top:32px;font-size:17.5px">What people says</div>
    <div class="underline" style="top:55px"></div>
    <svg class="chev" style="left:53px;top:123px" viewBox="0 0 10 16"><path d="M8 1 2 8l6 7" fill="none" stroke="#333" stroke-width="1.2"/></svg>
    <svg class="chev" style="left:436px;top:123px" viewBox="0 0 10 16"><path d="M2 1l6 7-6 7" fill="none" stroke="#333" stroke-width="1.2"/></svg>
    <div class="abs" style="left:113px;top:82px;width:279px;height:114px;background:var(--cream);border:1px solid var(--gold)">
      <div class="abs" style="inset:4px;border:1px solid #e0d2b7"></div>
      <div class="abs center serif" style="left:0;right:0;top:4px;font-size:30px;line-height:1;color:var(--gold)">“</div>
      <div class="lorem center" style="left:20px;right:20px;top:37px;font-size:6.4px;color:var(--ink)">Lorem ipsum dolor sit amet, consectetur adipiscing elit, sed do eiusmod tempor incididunt ut labore et dolore magna aliqua Quis ipsum suspendisse ultrices gravida Risus commodo viverra maecenas accumsan lacus vel facilisis.</div>
      <div class="abs center" style="left:0;right:0;top:82px;font-size:6.4px">-Jordan Ellis</div>
      <div class="abs center" style="left:0;right:0;top:92px;font-size:6px;color:var(--gold);letter-spacing:1px">★★★★★</div>
    </div>
  </section>

  <section class="section d-events">
    <div class="eyebrow left" style="left:55px;top:26px">Our resources —</div>
    <div class="title left" style="left:54px;top:34px;font-size:16px">Our Events</div>
    <div class="rule" style="left:55px;top:56px;width:30px"></div>
    <div class="photo ph-sunset" role="img" aria-label="Friends toasting with white wine at sunset" style="left:55px;top:77px;width:195px;height:163px"></div>
    <div class="abs" style="left:68px;top:203px;font-size:4px;color:#fff">15 SEP 2024</div>
    <div class="abs" style="left:68px;top:210px;width:170px;font-size:7px;line-height:1.35;color:#fff">Lorem ipsum dolor sit amet consectetur adipiscing elit sed do eiusmod</div>
    <div class="photo ph-laugh" role="img" aria-label="Two women laughing with wine glasses" style="left:256px;top:77px;width:98px;height:80px"></div>
    <div class="photo ph-dinner" role="img" aria-label="Dinner table with wine and dishes" style="left:256px;top:163px;width:98px;height:77px"></div>
    <div class="ev-date" style="left:363px;top:83px"><i></i>15 SEP 2024</div>
    <div class="ev-title" style="left:363px;top:92px;width:115px">Lorem ipsum dolor sit amet consectetur adipiscing</div>
    <div class="lorem" style="left:363px;top:111px;width:115px">Lorem ipsum dolor sit amet, consecte­tur adipiscing elit sed do</div>
    <div class="pill" style="left:363px;top:128px;width:36px;height:10px;font-size:3.6px">Learn More</div>
    <div class="ev-date" style="left:363px;top:168px"><i></i>15 SEP 2024</div>
    <div class="ev-title" style="left:363px;top:177px;width:115px">Lorem ipsum dolor sit amet consectetur adipiscing</div>
    <div class="lorem" style="left:363px;top:196px;width:115px">Lorem ipsum dolor sit amet, consecte­tur adipiscing elit sed do</div>
    <div class="pill" style="left:363px;top:213px;width:36px;height:10px;font-size:3.6px">Learn More</div>
  </section>

  <section class="section d-exp">
    <div class="photo ph-field" role="img" aria-label="Blurred vineyard rows at golden hour" style="inset:0"></div>
    <div class="photo ph-glass" role="img" aria-label="Glass of white wine" style="left:226px;top:147px;width:54px;height:150px;border-radius:26px 26px 4px 4px"></div>
    <div class="eyebrow" style="top:47px;font-size:6px">Explore our wine &amp; enjoy</div>
    <div class="title" style="top:56px;font-size:19px">Experience Our Wine</div>
    <div class="underline" style="top:81px"></div>
    <div class="pill" style="left:217px;top:103px;width:72px;height:18px;font-size:5.4px">View Wines ›</div>

    <div class="brand" style="left:50px;width:75px;top:318px">
      <div style="width:14px;height:14px;border:1px solid #fff;border-radius:50%;margin:0 auto 3px"></div>
      <div style="font-size:11px">TALVORA</div>
      <div style="font-size:4.6px;letter-spacing:2px">CELLARS</div>
    </div>
    <div class="social" style="left:66px;top:366px"><i style="width:9px;height:9px"></i><i style="width:9px;height:9px"></i><i style="width:9px;height:9px"></i><i style="width:9px;height:9px"></i></div>

    <div class="foot-head" style="left:166px;top:318px">Navigation</div>
    <div class="rule" style="left:166px;top:329px;width:40px"></div>
    <div class="foot-links" style="left:166px;top:333px">About us<br>Our Wines<br>Member Only<br>Annual Wines<br>Shop Wine</div>
    <div class="foot-head" style="left:266px;top:318px">Resources</div>
    <div class="rule" style="left:266px;top:329px;width:40px"></div>
    <div class="foot-links" style="left:266px;top:333px">My Account<br>Blogs<br>Terms of Use<br>Privacy Policy<br>Contact us</div>
    <div class="foot-head" style="left:363px;top:318px">Contact Us</div>
    <div class="rule" style="left:363px;top:329px;width:40px"></div>
    <svg class="abs" style="left:363px;top:340px" width="11" height="11" viewBox="0 0 12 12"><circle cx="6" cy="6" r="6" fill="#a98a5a"/><path d="M4 3.2c.4 2.3 1.9 3.9 4.4 4.6l.6-1-1.3-.7-.6.6c-.8-.4-1.5-1.1-1.9-1.9l.6-.6-.7-1.3z" fill="#fff"/></svg>
    <div class="abs" style="left:385px;top:340px;font-size:4.6px;color:var(--gold)">Phone Number</div>
    <div class="abs" style="left:385px;top:347px;font-size:5.4px;color:#fff">(+123) 456 7890</div>
    <svg class="abs" style="left:363px;top:367px" width="11" height="11" viewBox="0 0 12 12"><circle cx="6" cy="6" r="6" fill="#a98a5a"/><rect x="3" y="4" width="6" height="4.2" fill="none" stroke="#fff" stroke-width=".7"/><path d="M3 4l3 2.3L9 4" fill="none" stroke="#fff" stroke-width=".7"/></svg>
    <div class="abs" style="left:385px;top:366px;font-size:4.6px;color:var(--gold)">Email address</div>
    <div class="abs" style="left:385px;top:373px;font-size:5.2px;color:#fff;white-space:nowrap">enquiry@talvoracellars-demo.com</div>
    <div class="rule" style="left:62px;top:427px;width:381px;background:#333"></div>
    <div class="abs center" style="left:0;right:0;top:436px;font-size:4.6px;color:#bbb">Copyright © 2024 Talvora Cellars. All Right Reserved</div>
  </section>
</div>

<!-- Mobile layout -->
<div class="site site-mobile">

  <section class="section m-hero">
    <div class="photo" style="left:0;top:0;width:146px;height:110px;background:#0b0203"></div>
    <div class="photo ph-hero" role="img" aria-label="Red wine being poured into a glass" style="left:0;top:95px;width:146px;height:122px"></div>
    <div class="brand" style="left:48px;width:50px;top:5px">
      <div style="width:9px;height:9px;border:1px solid #fff;border-radius:50%;margin:0 auto 2px"></div>
      <div style="font-size:6.4px">TALVORA</div>
      <div style="font-size:2.8px;letter-spacing:1.2px">CELLARS</div>
    </div>
    <svg class="abs" style="left:128px;top:9px" width="9" height="6" viewBox="0 0 9 6"><path d="M0 .5h9M0 3h9M0 5.5h9" stroke="#a98a5a" stroke-width=".8"/></svg>
    <div class="eyebrow" style="top:50px;font-size:3.6px;letter-spacing:.8px">Introducing Talvora Cellars</div>
    <div class="title" style="top:56px;font-size:9.4px;line-height:1.2;color:#fff">Because wine<br>should be<br>an experience</div>
    <div class="underline" style="top:93px;width:24px;margin-left:-12px;background:#fff"></div>
    <div class="abs" style="left:72px;top:200px;width:1px;height:22px;background:var(--gold-light)"></div>
  </section>

  <section class="section m-featured">
    <div class="eyebrow" style="top:20px;font-size:3.4px;letter-spacing:.8px">— Talvora Cellars Wine —</div>
    <div class="title" style="top:27px;font-size:10.4px">Featured Wines</div>
    <div class="underline" style="top:42px;width:24px;margin-left:-12px"></div>
    <div class="f-card" style="left:34px;top:71px;width:82px;height:122px">
      <div class="bottle green" role="img" aria-label="Sparkling wine bottle" style="top:-12px;width:20px;margin-left:-10px;height:86px"></div>
      <div class="name" style="top:80px;font-size:4px">WINE HEADING</div>
      <div class="lorem" style="top:87px;left:8px;right:8px;font-size:3.2px">Lorem ipsum dolor sit amet consec­tetur adipiscing elit sed</div>
      <div class="pill" style="top:104px;left:26px;width:30px;height:7px;font-size:2.6px">Shop Wine</div>
    </div>
    <div class="rule" style="top:209px;left:58px;width:10px;background:#999"></div>
    <div class="rule" style="top:209px;left:74px;width:10px;height:1.5px;background:var(--gold)"></div>
    <div class="pill outline" style="top:218px;left:42px;width:62px;height:16px;font-size:4.2px">View All ›</div>
  </section>

  <section class="section m-maker">
    <div class="photo ph-toast" role="img" aria-label="Friends toasting with wine at a vineyard table" style="left:10px;top:20px;width:125px;height:125px;border-radius:50%;border:3px solid var(--gold)"></div>
    <div class="eyebrow left" style="left:15px;top:158px;font-size:3.4px;letter-spacing:.8px">About our wines —</div>
    <div class="title left" style="left:14px;top:167px;font-size:9.6px;line-height:1.25">Message from the<br>Winemaker</div>
    <div class="rule" style="left:15px;top:197px;width:22px"></div>
    <div class="lorem" style="left:16px;top:207px;width:116px;font-size:3.5px;color:var(--ink)">I started my winemaking journey with one simple goal in mind - I wanted to make wine as good or better than the wine I could buy. At the time of that goal in 2015, I had no perspec­tive on the path that would form before me. Enjoy...the experience.</div>
    <div class="photo ph-face" role="img" aria-label="Portrait of the winemaker" style="left:14px;top:264px;width:20px;height:20px;border-radius:50%"></div>
    <div class="photo ph-sign" role="img" aria-label="Handwritten signature of Julian Talvora" style="left:38px;top:270px;width:62px;height:10px"></div>
  </section>

  <section class="section m-cats">
    <div class="m-cat" style="top:15px;background:var(--wine)">
      <div class="title">Red Wine</div>
      <div class="lorem">Lorem ipsum dolor sit amet, consecte­tur adipiscing elit, sed do</div>
      <div class="pill outline-light">Try it now</div>
      <div class="photo ph-redpair" role="img" aria-label="Glass of red wine beside a red wine bottle" style="left:36px;top:62px;width:38px;height:77px;border-radius:12px 12px 0 0"></div>
    </div>
    <div class="m-cat" style="top:166px;background:var(--gold-mid)">
      <div class="title">White Wine</div>
      <div class="lorem">Lorem ipsum dolor sit amet, consecte­tur adipiscing elit, sed do</div>
      <div class="pill outline-light">Try it now</div>
      <div class="photo ph-whitepair" role="img" aria-label="Glass of white wine beside a white wine bottle" style="left:36px;top:62px;width:38px;height:77px;border-radius:12px 12px 0 0"></div>
    </div>
    <div class="m-cat" style="top:317px;background:var(--gold-deep)">
      <div class="title">Summer Series</div>
      <div class="lorem">Lorem ipsum dolor sit amet, consecte­tur adipiscing elit, sed do</div>
      <div class="pill outline-light">Try it now</div>
      <div class="photo ph-sparkpair" role="img" aria-label="Glass of sparkling wine beside a sparkling bottle" style="left:36px;top:62px;width:38px;height:77px;border-radius:12px 12px 0 0"></div>
    </div>
  </section>

  <section class="section m-member" style="background:#141413">
    <div class="photo ph-club" role="img" aria-label="Friends raising wine glasses in a vineyard" style="left:0;top:0;width:146px;height:165px"></div>
    <div class="eyebrow left" style="left:14px;top:152px;color:#fff;font-size:3.6px;letter-spacing:.8px">Our wine club</div>
    <div class="title left" style="left:14px;top:159px;font-size:11.4px;color:#fff">Member Only</div>
    <div class="lorem" style="left:14px;top:177px;width:120px;font-size:3.8px;color:#fff">Lorem ipsum dolor sit amet, consectetur adipi­scing elit, sed do eiusmod tempor incididunt ut labore et dolore magna aliqua. o eiusmod tempor incididunt ut labore</div>
    <div class="pill" style="left:14px;top:217px;width:50px;height:11px;font-size:3.4px">Read More ›</div>
  </section>

  <section class="section m-annual">
    <div class="eyebrow" style="top:21px;font-size:3.4px;letter-spacing:.8px">— Talvora Cellars Wine —</div>
    <div class="title" style="top:28px;font-size:10.4px">Annual Wines</div>
    <div class="underline" style="top:43px;width:24px;margin-left:-12px"></div>
    <svg class="chev" style="left:5px;top:124px;width:7px;height:12px" viewBox="0 0 10 16"><path d="M8 1 2 8l6 7" fill="none" stroke="#777" stroke-width="1.2"/></svg>
    <svg class="chev" style="left:133px;top:124px;width:7px;height:12px" viewBox="0 0 10 16"><path d="M2 1l6 7-6 7" fill="none" stroke="#777" stroke-width="1.2"/></svg>
    <div class="arch" style="left:23px;top:59px;width:100px;height:131px;border-radius:50px 50px 0 0">
      <div class="bottle white" role="img" aria-label="White wine bottle" style="top:8px;width:20px;margin-left:-10px;height:74px"></div>
      <div class="name" style="top:85px;font-size:4px">WINE HEADING</div>
      <div class="lorem" style="top:92px;left:14px;right:14px;font-size:3.1px">Lorem ipsum dolor sit amet consec­tetur adipiscing elit sed</div>
      <div class="pill" style="top:108px;left:30px;width:40px;height:7px;font-size:2.6px">Shop Wine</div>
    </div>
  </section>

  <section class="section m-testi">
    <div class="photo ph-valley" role="img" aria-label="Hazy mountains above vineyard rows" style="inset:0"></div>
    <div class="eyebrow" style="top:18px;font-size:3.2px;letter-spacing:.8px">— Testimonials —</div>
    <div class="title" style="top:24px;font-size:10.4px">What people says</div>
    <div class="underline" style="top:39px;width:24px;margin-left:-12px"></div>
    <div class="abs" style="left:11px;top:60px;width:126px;height:111px;background:var(--cream);border:1px solid var(--gold)">
      <div class="abs center serif" style="left:0;right:0;top:2px;font-size:20px;line-height:1;color:var(--gold)">“</div>
      <div class="lorem center" style="left:8px;right:8px;top:24px;font-size:3.5px;color:var(--ink)">Lorem ipsum dolor sit amet, consectetur adipi­scing elit, sed do eiusmod tempor incididunt ut labore et dolore magna aliqua Quis ipsum sus­pendisse ultrices gravida Risus commodo viver­ra maecenas accumsan lacus vel facilisis.</div>
      <div class="abs center" style="left:0;right:0;top:77px;font-size:4px">-Jordan Ellis</div>
      <div class="abs center" style="left:0;right:0;top:84px;font-size:4px;color:var(--gold);letter-spacing:.6px">★★★★★</div>
    </div>
  </section>

  <section class="section m-events">
    <div class="eyebrow left" style="left:9px;top:15px;font-size:3.4px;letter-spacing:.8px">Our resources —</div>
    <div class="title left" style="left:9px;top:21px;font-size:10.4px">Our Events</div>
    <div class="rule" style="left:9px;top:37px;width:22px"></div>
    <div class="photo ph-sunset" role="img" aria-label="Friends toasting with white wine at sunset" style="left:9px;top:51px;width:126px;height:101px"></div>
    <div class="abs" style="left:16px;top:128px;width:110px;font-size:4px;line-height:1.3;color:#fff">Lorem ipsum dolor sit amet consectetur adipiscing elit sed do eiusmod</div>
    <div class="photo ph-laugh" role="img" aria-label="Two women laughing with wine glasses" style="left:9px;top:157px;width:61px;height:47px"></div>
    <div class="photo ph-dinner" role="img" aria-label="Dinner table with wine and dishes" style="left:9px;top:209px;width:61px;height:47px"></div>
    <div class="ev-date" style="left:75px;top:160px;font-size:2.6px"><i style="width:3px;height:3px"></i>15 SEP 2024</div>
    <div class="ev-title" style="left:75px;top:166px;width:62px;font-size:3.8px">Lorem ipsum dolor sit amet consectetur adipiscing</div>
    <div class="lorem" style="left:75px;top:177px;width:62px;font-size:2.8px">Lorem ipsum dolor sit amet, consecte­tur adipiscing elit sed do</div>
    <div class="pill" style="left:75px;top:190px;width:24px;height:6px;font-size:2.4px">Learn More</div>
    <div class="ev-date" style="left:75px;top:212px;font-size:2.6px"><i style="width:3px;height:3px"></i>15 SEP 2024</div>
    <div class="ev-title" style="left:75px;top:218px;width:62px;font-size:3.8px">Lorem ipsum dolor sit amet consectetur adipiscing</div>
    <div class="lorem" style="left:75px;top:229px;width:62px;font-size:2.8px">Lorem ipsum dolor sit amet, consecte­tur adipiscing elit sed do</div>
    <div class="pill" style="left:75px;top:242px;width:24px;height:6px;font-size:2.4px">Learn More</div>
  </section>

  <section class="section m-exp" style="background:#0c0c0c">
    <div class="abs" style="left:0;top:0;width:146px;height:65px;background:#f4f1ea"></div>
    <div class="photo" role="img" aria-label="Blurred golden vineyard" style="left:0;top:65px;width:146px;height:155px;background:linear-gradient(180deg,#b8ad6a 0%,#8a8a32 25%,#5f6a22 50%,#2f3413 75%,#0c0c0c 100%)"></div>
    <div class="photo ph-glass" role="img" aria-label="Glass of white wine" style="left:55px;top:100px;width:36px;height:92px;border-radius:17px 17px 3px 3px"></div>
    <div class="eyebrow" style="top:19px;font-size:3.6px;letter-spacing:.8px">Explore our wine &amp; enjoy</div>
    <div class="title" style="top:27px;font-size:11.2px;line-height:1.15">Experience<br>Our Wine</div>
    <div class="underline" style="top:57px;width:24px;margin-left:-12px"></div>
    <div class="pill" style="left:48px;top:82px;width:50px;height:11px;font-size:3.4px">View Wines ›</div>

    <div class="brand" style="left:48px;width:50px;top:234px">
      <div style="width:9px;height:9px;border:1px solid #fff;border-radius:50%;margin:0 auto 2px"></div>
      <div style="font-size:7px">TALVORA</div>
      <div style="font-size:3px;letter-spacing:1.2px">CELLARS</div>
    </div>
    <div class="social" style="left:60px;top:258px"><i style="width:5.5px;height:5.5px"></i><i style="width:5.5px;height:5.5px"></i><i style="width:5.5px;height:5.5px"></i><i style="width:5.5px;height:5.5px"></i></div>
    <div class="foot-head center" style="left:0;right:0;top:274px;font-size:5px">Navigation</div>
    <div class="foot-links center" style="left:0;right:0;top:283px;font-size:3.3px;line-height:2.3">About us<br>Our Wines<br>Member Only<br>Annual Wines<br>Shop Wine</div>
    <div class="foot-head center" style="left:0;right:0;top:338px;font-size:5px">Resources</div>
    <div class="foot-links center" style="left:0;right:0;top:347px;font-size:3.3px;line-height:2.3">My Account<br>Blogs<br>Terms of Use<br>Privacy Policy<br>Contact us</div>
    <div class="foot-head center" style="left:0;right:0;top:403px;font-size:5px">Contact Us</div>
    <svg class="abs" style="left:36px;top:418px" width="8" height="8" viewBox="0 0 12 12"><circle cx="6" cy="6" r="6" fill="#a98a5a"/><path d="M4 3.2c.4 2.3 1.9 3.9 4.4 4.6l.6-1-1.3-.7-.6.6c-.8-.4-1.5-1.1-1.9-1.9l.6-.6-.7-1.3z" fill="#fff"/></svg>
    <div class="abs" style="left:48px;top:417px;font-size:3px;color:var(--gold)">Phone Number</div>
    <div class="abs" style="left:48px;top:422px;font-size:3.4px;color:#fff">(+123) 456 7890</div>
    <svg class="abs" style="left:36px;top:440px" width="8" height="8" viewBox="0 0 12 12"><circle cx="6" cy="6" r="6" fill="#a98a5a"/><rect x="3" y="4" width="6" height="4.2" fill="none" stroke="#fff" stroke-width=".7"/><path d="M3 4l3 2.3L9 4" fill="none" stroke="#fff" stroke-width=".7"/></svg>
    <div class="abs" style="left:48px;top:439px;font-size:3px;color:var(--gold)">Email address</div>
    <div class="abs" style="left:48px;top:444px;font-size:3.1px;color:#fff;white-space:nowrap">enquiry@talvoracellars-demo.com</div>
    <div class="abs center" style="left:0;right:0;top:470px;font-size:2.8px;color:#bbb">Copyright © 2024 Talvora Cellars. All Right Reserved</div>
  </section>
</div>

</div>
</body>
</html>
```